Tri-Fold Brochure Redesign for Floral Preservation Business

I would like to redesign my current tri-fold brouchue that I created myself and have it updated. I would like to keep the same content, color and images, but have it redesigned to look fresher and updated. I'm in the the floral preservation business and work with brides in the wedding inductry. I'm looking for a royal/rustic feel and it should relate to the look and feel of my website www.larkmeadow.com. I have included the Photoshop file I used to create my orginal bouchure.

The only content that has changed is my address which is now;
2847 Birchfall Court, Reston VA 20173

Safe Zone Width - 10.875
Safe Zone Height - 8.375

I have included the Photoshop and Illustrator templates for the tri-fold brochure from the printer I will be using.

```html
<!DOCTYPE html>
<html lang="en">
<head>
<meta charset="utf-8">
<title>Larkmeadow Tri-Fold Brochure</title>
<link rel="stylesheet" href="https://fonts.googleapis.com/css2?family=Arimo:wght@400;700&family=Great+Vibes&display=swap">
<style>
  :root {
    --crimson: #d21f3c;
    --crimson-dark: #b8172f;
    --ink: #4a4a4a;
    --paper: #ffffff;
    --mist: #e6e6e6;
    --mist-dark: #c9c9c9;
    --stage: #8f8f8f;
    --stage-dark: #5f5f5f;
  }
  * { box-sizing: border-box; margin: 0; padding: 0; }
  html, body { width: 1200px; height: 1000px; overflow: hidden; }
  body {
    background: radial-gradient(ellipse at 50% 40%, var(--stage) 0%, var(--stage-dark) 100%);
    font-family: "Arimo", Arial, sans-serif;
    color: var(--ink);
    position: relative;
  }
  .brochure {
    position: absolute; left: 50px; top: 75px;
    width: 1100px; height: 850px;
    background: var(--paper);
    box-shadow: 0 6px 24px rgba(0,0,0,.35);
    overflow: hidden;
  }
  .swirl-field {
    position: absolute; left: 0; top: 0; width: 733px; height: 850px;
    background: radial-gradient(ellipse at 20% 85%, #efefef 0%, rgba(255,255,255,0) 55%),
                radial-gradient(ellipse at 70% 55%, #f2f2f2 0%, rgba(255,255,255,0) 50%);
  }
  .banner { position: absolute; left: 0; top: 0; width: 733px; height: 190px; }
  .banner svg { display: block; }
  .banner-headline {
    position: absolute; left: 40px; right: 40px; top: 42px;
    color: #fff; font-weight: 700; font-size: 17.5px; line-height: 1.3;
    text-align: center;
  }
  .photo {
    position: absolute; border-radius: 2px;
  }
  .photo-shadowbox {
    left: 70px; top: 190px; width: 235px; height: 310px;
    background: linear-gradient(135deg, #5a1a17 0%, #3a0f0d 100%);
    padding: 18px;
  }
  .photo-shadowbox .mat {
    width: 100%; height: 100%;
    background: radial-gradient(ellipse at 50% 40%, #f3ecd9 0%, #d8cbb0 100%);
  }
  .photo-bracelet {
    left: 390px; top: 590px; width: 310px; height: 190px;
    background: radial-gradient(ellipse at 50% 50%, #7ab4d8 0%, #b9d6e8 45%, #ffffff 75%);
  }
  .section-title {
    position: absolute; color: var(--crimson); font-weight: 700; font-size: 24px;
    text-align: center;
  }
  .ornament {
    position: absolute; height: 18px; width: 90px;
    background: linear-gradient(90deg, rgba(210,31,60,0) 0%, var(--crimson) 50%, rgba(210,31,60,0) 100%);
    opacity: .55; border-radius: 9px;
  }
  .body-copy {
    position: absolute; font-size: 12.5px; line-height: 1.5; color: var(--ink);
  }
  .process-panel {
    position: absolute; left: 733px; top: 0; width: 367px; height: 850px;
    background: linear-gradient(180deg, var(--mist) 0%, #d7d7d7 100%);
    text-align: center; color: var(--ink);
  }
  .process-panel .swirl-field { width: 100%; background: radial-gradient(ellipse at 30% 40%, #f1f1f1 0%, rgba(255,255,255,0) 60%); }
  .process-title {
    position: relative; margin-top: 40px; color: var(--crimson);
    font-weight: 700; font-size: 26px;
  }
  .process-panel .ornament { position: relative; margin: 6px auto 0; display: block; }
  .step { position: relative; padding: 0 34px; }
  .step-number {
    font-family: "Great Vibes", cursive; font-size: 30px; color: #6d6d6d;
    margin-top: 18px; line-height: 1;
  }
  .step-title { color: var(--crimson); font-weight: 700; font-size: 19px; margin: 4px 0 6px; }
  .step-copy { font-size: 12.5px; line-height: 1.45; }
  .closing-ornament { margin-top: 26px !important; width: 130px !important; }
  .closing-note {
    position: relative; margin-top: 40px; padding: 0 50px;
    font-size: 12.5px; line-height: 1.4; color: #333;
  }
</style>
</head>
<body>
  <main class="brochure">
    <div class="swirl-field" role="img" aria-label="Faint grey floral swirl pattern"></div>

    <header class="banner">
      <svg width="733" height="190" viewBox="0 0 733 190" aria-hidden="true">
        <path d="M0 0 H733 V170 Q560 115 366 118 Q170 122 0 175 Z" fill="var(--crimson)"/>
      </svg>
      <h1 class="banner-headline">You Have Chosen The Perfect Flowers, Now Choose The Perfect Way To Cherish Them. Larkmeadow's Floral Preservation Process Transforms Your Flowers Into Lasting Works of Art or Jewelry</h1>
    </header>

    <div class="photo photo-shadowbox" role="img" aria-label="Framed shadowbox holding a preserved ivory bridal bouquet with white ribbon">
      <div class="mat"></div>
    </div>

    <h2 class="section-title" style="left:40px; width:300px; top:525px;">Floral Preservation</h2>
    <div class="ornament" style="left:145px; top:560px;" role="img" aria-label="Red flourish ornament"></div>
    <p class="body-copy" style="left:40px; width:300px; top:590px;">Our handcrafted shadowboxes are made with the industries finest raw materials to ensure the highest level of quality. We exclusively offer Harrow-Vale moulding, makers of beautiful moulding for over 100 years. Using archival standards set by the National Archive Guild, our shadowboxes are matted and mounted with the Elmhurst FrameGuard system. This system is used by museums to protect some of this nation's most valuable artwork. We finish by using ClearVale's Gallery glass to enhance, protect and beautify. Each of these details contributes to a museum-quality work of art.</p>

    <h2 class="section-title" style="left:385px; width:320px; top:225px;">Flower-Petal Jewelry</h2>
    <div class="ornament" style="left:500px; top:260px;" role="img" aria-label="Red flourish ornament"></div>
    <p class="body-copy" style="left:400px; width:295px; top:292px;">If you would like to turn your memories into a wearable story, consider creating signature jewelry. We turn real petals from your blooms into one-of-a-kind jewelry pieces for you or your loved ones. We can transform your flowers into earrings, necklaces, bracelets, Bellmore- and Kestrel-type charms or rosaries. The tradition hails from the historical practice of nuns creating rosaries from condensed flower petals. In that same vein, we create unique pieces to fit your own style. Each piece is made by hand from your flowers and the highest quality sterling silver findings.</p>

    <div class="photo photo-bracelet" role="img" aria-label="Flower-petal bracelet with blue marbled beads and silver findings"></div>

    <section class="process-panel">
      <div class="swirl-field" role="img" aria-label="Faint grey floral swirl pattern"></div>
      <h2 class="process-title">THE PROCESS</h2>
      <div class="ornament" role="img" aria-label="Red flourish ornament"></div>

      <div class="step">
        <p class="step-number">Step1</p>
        <h3 class="step-title">Reserve The Date</h3>
        <p class="step-copy">To ensure our services, you will need to "reserve the date" with a deposit. We accept no more than 4 clients a week and with over 50,000 weddings in the DC and Hampton Roads Metro areas annually, many brides reserve their wedding date up to four months in advance. The full deposit is applied to the cost of your final design selection.</p>
      </div>
      <div class="step">
        <p class="step-number">Step2</p>
        <h3 class="step-title">Secure The Flowers</h3>
        <p class="step-copy">You can either drop your flowers off shortly after the event, or we can pick them up the night of the reception. Is your event out of town? No problem. You can ship them to us overnight or drop them off upon your return.</p>
      </div>
      <div class="step">
        <p class="step-number">Step3</p>
        <h3 class="step-title">Design Selection</h3>
        <p class="step-copy">Within 30 days after your event we ask that you make an appointment to visit our showroom to make your final design selection. Once your order has been placed, it takes approximately 2 to 3 months to complete.</p>
      </div>

      <div class="ornament closing-ornament" role="img" aria-label="Red flourish ornament"></div>
      <p class="closing-note">Please visit our website for full details, pricing and additional pictures.<br>www.larkmeadow.com</p>
    </section>
  </main>
</body>
</html>
```